MOSLEN Environmental needs an upgrade to its current business cards design

We need an upgrade to our current business cards design, where the MOSLEN acronym is included, as possible and not being overloaded.
MOSLEN Environmental is an Environmental Consultancy Firm based in Sydney.
We would like to see creative designs different from the standard type of business cards (for example, rounded edges, different to standard size of common business cards.

Target Market(s)

industrial companies (oil & gas, petrochemical, mining, insolvency, finance and manufacturing), developers, architect firms, law firms.

Industry/Entity Type

Business

Contact Information for Business Card

logos (brand and acronym), if they don't appear overloaded.
name
role
name of company (MOSLEN Environmental),
address (Level 3, Suite 3C, 47-49 Dorrigan Lane, Wexmoor, NSW, 2188) landline (02 7314 2986)
mobile (staff member)
email (staff member) and
website (www.moslengreen.example).
Include: Contaminated Land, Site Remediation, Groundwater Assessment, Health and Ecological Risk Assessments, Acid Sulfate Soils, Waste Classification.

Font styles to use
Serif
Sans Serif

Requirements
Must have
• A creative design different to the standard type of business cards.
Nice to have
• Rounded edges
• Different size of business cards rather than the standard size.
Should not have
• Preferable not to use white colour background, unless it is required from a creative design proposed.
• Not an overloaded design.
• Avoid black colours

```html
<!DOCTYPE html>
<html lang="en">
<head>
<meta charset="utf-8">
<title>MOSLEN Environmental – Business Card</title>
<link rel="stylesheet" href="https://fonts.googleapis.com/css2?family=Oswald:wght@500;700&family=Roboto+Condensed:wght@700&family=Arimo:wght@700&display=swap">
<style>
  :root{
    --card:#373737;
    --green:#7fc31c;
    --grey-dark:#5b5b5b;
    --grey-mid:#6a6a6a;
    --grey-light:#d2d3d4;
    --text-light:#dedede;
    --page:#ffffff;
  }
  *{box-sizing:border-box;margin:0;padding:0}
  html,body{width:1200px;height:1200px;overflow:hidden;background:var(--page)}
  .sheet{position:absolute;left:0;top:0;width:1500px;height:1500px;transform:scale(.8);transform-origin:0 0}
  .card{position:absolute;left:320px;width:868px;height:496px;background:var(--card);overflow:hidden}
  .card--front{top:222px}
  .card--back{top:732px}
  .card svg.deco{position:absolute;inset:0;width:100%;height:100%}

  /* front */
  .brand{position:absolute;left:95px;width:552px;top:52px;text-align:center;font-family:"Oswald",sans-serif;font-weight:700;line-height:1}
  .brand__name{display:block;font-size:160px;letter-spacing:6px;color:var(--green)}
  .brand__sub{display:block;font-size:46px;letter-spacing:11px;margin-top:8px;color:var(--green)}
  .rule{position:absolute;height:4px;background:var(--grey-light);border-radius:2px}
  .card--front .rule{left:32px;width:678px;top:344px}
  .services{position:absolute;left:20px;width:700px;top:372px;text-align:center;color:var(--green);font-family:"Arimo",sans-serif;font-weight:700;font-size:19px;line-height:29.5px}
  .services .sep{color:var(--text-light);font-size:12px;margin:0 10px;vertical-align:2px}

  /* back: acronym */
  .acronym{position:absolute;left:36px;top:92px;list-style:none}
  .acronym li{display:flex;align-items:center;height:52px}
  .acronym__letter{width:58px;font-family:"Oswald",sans-serif;font-weight:700;font-size:50px;line-height:1;color:var(--green)}
  .acronym__word{font-family:"Arimo",sans-serif;font-weight:700;font-size:21px;color:var(--grey-mid);letter-spacing:-.3px}

  /* back: details */
  .details{position:absolute;left:390px;width:440px;top:32px;text-align:center;font-family:"Roboto Condensed",sans-serif;font-weight:700;white-space:nowrap}
  .person{color:var(--green);font-family:"Oswald",sans-serif;font-weight:500;font-size:30px;letter-spacing:6px;line-height:42px}
  .company{margin-top:18px;color:var(--text-light);font-size:23px;letter-spacing:3.5px}
  .address{margin-top:6px;color:var(--text-light);font-size:18px;letter-spacing:2px;line-height:25px}
  .contacts{position:absolute;left:534px;top:236px;list-style:none}
  .contacts li{display:flex;align-items:center;height:64px;color:var(--text-light);font-family:"Arimo",sans-serif;font-weight:700;font-size:20px;letter-spacing:3.4px;white-space:nowrap}
  .contacts svg{width:48px;height:48px;margin-right:12px;flex:none}
  .contacts__link{position:absolute;left:556px;top:278px;width:4px;height:90px;background:var(--green)}
  .card--back .rule{left:412px;width:406px;top:428px}
  .website{position:absolute;left:402px;width:426px;top:448px;text-align:center;color:var(--green);font-family:"Arimo",sans-serif;font-weight:700;font-size:21px;letter-spacing:4.6px;white-space:nowrap}
</style>
</head>
<body>
<main class="sheet">

  <section class="card card--front" aria-label="Card front">
    <svg class="deco" viewBox="0 0 868 496" preserveAspectRatio="none" aria-hidden="true">
      <path d="M868 0 C835 140 735 250 742 350 C748 420 790 470 802 496 L868 496 Z" fill="var(--green)"/>
      <path d="M868 226 C830 310 796 370 800 430 C803 465 818 486 828 496 L868 496 Z" fill="var(--grey-light)"/>
      <path d="M868 360 C842 400 830 440 836 470 C840 484 846 492 850 496 L868 496 Z" fill="var(--grey-dark)"/>
    </svg>
    <h1 class="brand"><span class="brand__name">MOSLEN</span><span class="brand__sub">ENVIRONMENTAL</span></h1>
    <div class="rule"></div>
    <p class="services">
      Contaminated Land<span class="sep">◆</span>Site Remediation<span class="sep">◆</span>Groundwater Assessment<br>
      Health and Ecological Risk Assessments<span class="sep">◆</span>Acid Sulfate Soils<br>
      Waste Classification
    </p>
  </section>

  <section class="card card--back" aria-label="Card back">
    <svg class="deco" viewBox="0 0 868 496" preserveAspectRatio="none" aria-hidden="true">
      <path d="M316 0 C372 110 362 250 350 340 C340 420 318 470 316 496" fill="none" stroke="var(--grey-dark)" stroke-width="10"/>
      <path d="M306 0 C362 110 352 250 340 340 C330 420 308 470 306 496" fill="none" stroke="var(--grey-light)" stroke-width="10"/>
      <path d="M295 0 C351 110 341 250 329 340 C319 420 297 470 295 496" fill="none" stroke="var(--green)" stroke-width="12"/>
    </svg>

    <ul class="acronym">
      <li><span class="acronym__letter">M</span><span class="acronym__word">ONITORING</span></li>
      <li><span class="acronym__letter">O</span><span class="acronym__word">VERSIGHT (OF)</span></li>
      <li><span class="acronym__letter">S</span><span class="acronym__word">OIL</span></li>
      <li><span class="acronym__letter">L</span><span class="acronym__word">AND (AND)</span></li>
      <li><span class="acronym__letter">E</span><span class="acronym__word">COLOGICAL</span></li>
      <li><span class="acronym__letter">N</span><span class="acronym__word">ETWORKS</span></li>
    </ul>

    <div class="details">
      <p class="person">ROWAN KELBY<br>PROJECT ENGINEER</p>
      <p class="company">MOSLEN ENVIRONMENTAL</p>
      <p class="address">LEVEL 3, SUITE 3C, 47-49 DORRIGAN<br>LANE, WEXMOOR, NSW, 2188</p>
    </div>

    <div class="contacts__link"></div>
    <ul class="contacts">
      <li>
        <svg viewBox="0 0 48 48" aria-hidden="true"><circle cx="24" cy="24" r="21" fill="var(--card)" stroke="var(--green)" stroke-width="3"/><path d="M17 14 l4 -1 l3 6 l-3 2 c1 3 3 6 6 7 l2 -3 l6 3 l-1 4 c-9 1 -18 -8 -17 -18 z" fill="var(--text-light)"/></svg>
        02 7314 2986
      </li>
      <li>
        <svg viewBox="0 0 48 48" aria-hidden="true"><circle cx="24" cy="24" r="21" fill="var(--card)" stroke="var(--green)" stroke-width="3"/><rect x="17" y="12" width="14" height="24" rx="2" fill="none" stroke="var(--text-light)" stroke-width="2"/><line x1="22" y1="32" x2="26" y2="32" stroke="var(--text-light)" stroke-width="2"/></svg>
        123456
      </li>
      <li>
        <svg viewBox="0 0 48 48" aria-hidden="true"><circle cx="24" cy="24" r="21" fill="var(--card)" stroke="var(--green)" stroke-width="3"/><rect x="13" y="17" width="22" height="15" fill="var(--text-light)"/><path d="M13 17 l11 9 l11 -9" fill="none" stroke="var(--card)" stroke-width="2"/></svg>
        rk@moslen.example
      </li>
    </ul>

    <div class="rule"></div>
    <p class="website">www.moslengreen.example</p>
  </section>

</main>
</body>
</html>
```